Maple drift now Banner promoting freedom and adventure working from laptop

I need 3 different banners in 4 different sizes
I am an online business working from home on my laptop. I am in the motivational program and internet marketing industry and would like some banners that reflect healthy, fun and financially free lifestyle.
I have a Pallorum page title of KeyUpVibe and a website called Mapledriftnow.com
I have uploaded some photos but am unsure what may be required for the banners.
I am on the Gold Coast Australia but will be advertising in America, UK, Canada etc.

Target Market(s)

Adventure and Health fitness

Colors

Designer to choose colors to be used in the design.

Requirements
Must have
• Promotion of a living a financially free life through the ability of working from home via your own online business.
• Fun fit healthy freedom and adventure associated with someone living their dream life from working from home away from the 9 to 5 hustle and bussle.
Nice to have
• beaches, mountains and working from a Zen slate max.
• Showing fun and adventure from someone living this lifestyle.

```html
<!DOCTYPE html>
<html lang="en">
<head>
<meta charset="utf-8">
<title>Maple drift now – Work from Home banner</title>
<link href="https://fonts.googleapis.com/css2?family=Bree+Serif&display=swap" rel="stylesheet">
<style>
  :root {
    --page-bg: #f2f3f3;
    --cyan: rgba(22, 220, 234, 0.9);
    --lime: rgba(160, 232, 18, 0.92);
    --white: #ffffff;
    --forest-dark: #3f6a2c;
    --forest-mid: #7fa64f;
    --haze: #e7ece6;
    --wood: #a98562;
    --desk-dark: #2a2f36;
  }
  * { box-sizing: border-box; margin: 0; padding: 0; }
  html, body {
    width: 1200px; height: 1200px; overflow: hidden;
    background: var(--page-bg);
    font-family: "Bree Serif", Georgia, serif;
  }
  .banner {
    position: absolute; left: 10px; top: 382px;
    width: 1180px; height: 435px; overflow: hidden;
    color: var(--white);
  }
  .photo-nature {
    position: absolute; left: 0; top: 0; width: 720px; height: 100%;
    background:
      linear-gradient(180deg, var(--forest-dark) 0%, var(--forest-mid) 70%, #8cbc5a 100%);
    -webkit-mask-image: linear-gradient(90deg, #000 60%, transparent 100%);
            mask-image: linear-gradient(90deg, #000 60%, transparent 100%);
  }
  .photo-desk {
    position: absolute; left: 0; top: 0; width: 100%; height: 100%;
    background:
      linear-gradient(90deg, var(--haze) 45%, rgba(231,236,230,0) 62%),
      linear-gradient(160deg, #f4f4f2 0%, #e9e6e0 35%, var(--wood) 70%, var(--desk-dark) 100%);
  }
  .circle {
    position: absolute; border-radius: 50%;
    display: flex; flex-direction: column; align-items: center; justify-content: center;
    text-align: center; line-height: 1;
  }
  .circle--headline {
    left: 174px; top: 44px; width: 346px; height: 346px;
    background: var(--cyan);
  }
  .circle--lifestyle {
    left: 508px; top: 104px; width: 254px; height: 254px;
    background: var(--lime);
  }
  .headline-work { font-size: 62px; }
  .headline-home-row { display: flex; align-items: baseline; gap: 8px; margin-top: 2px; }
  .headline-from { font-size: 34px; }
  .headline-home { font-size: 70px; }
  .headline-with { font-size: 28px; margin-top: 10px; }
  .headline-devices { font-size: 34px; margin-top: 12px; }
  .lifestyle-create { font-size: 32px; }
  .lifestyle-word { font-size: 48px; margin-top: 8px; }
  .lifestyle-wanted { font-size: 26px; margin-top: 12px; line-height: 1.25; }
  .contact {
    position: absolute; left: 924px; top: 340px;
    display: flex; flex-direction: column; gap: 14px;
    font-size: 21px;
  }
  .contact-item { display: flex; align-items: center; gap: 10px; }
  .contact-mark { width: 24px; height: 24px; background: var(--white); flex: none; }
  .contact-mark--round { border-radius: 50%; }
</style>
</head>
<body>
  <section class="banner">
    <div class="photo-desk" role="img" aria-label="Photo of a person working on a laptop at a wooden desk with books, a notebook and a coffee cup"></div>
    <div class="photo-nature" role="img" aria-label="Photo of a man with arms raised standing under a large arching tree on green grass"></div>

    <div class="circle circle--headline">
      <div class="headline-work">Work</div>
      <div class="headline-home-row">
        <span class="headline-from">from</span>
        <span class="headline-home">Home</span>
      </div>
      <div class="headline-with">with your</div>
      <div class="headline-devices">Laptop &amp; Phone</div>
    </div>

    <div class="circle circle--lifestyle">
      <div class="lifestyle-create">Create the</div>
      <div class="lifestyle-word">Lifestyle</div>
      <div class="lifestyle-wanted">you always<br>wanted</div>
    </div>

    <div class="contact">
      <div class="contact-item"><span class="contact-mark contact-mark--round"></span>Mapledriftnow.com</div>
      <div class="contact-item"><span class="contact-mark"></span>KeyUpVibe</div>
    </div>
  </section>
</body>
</html>
```